Law firm business cards and stationary
Traditional professional presentation
Law firm business cards and stationary - Law
Creative Brief
Use same font as used in my logo
Other traditional looking fonts will be considered
Professional
Marla J. Pettigrew
Attorney at Law
742 E. 9th Ave, Ste 114 Spokane, WA 99208
(509) TRY-CASE
barrister@mailwove.com
roadcasedefenders.org
Please see uploaded logo. The phone number (509) TRY-CASE is displayed prominently in all marketing. Thank you.

```html
<!DOCTYPE html>
<html lang="en">
<head>
<meta charset="utf-8">
<title>The Pettigrew Firm – Business Card</title>
<link href="https://fonts.googleapis.com/css2?family=Cinzel:wght@400;600&display=swap" rel="stylesheet">
<style>
  :root {
    --bg: #e6e4e0;
    --card: #ffffff;
    --card-shade: #eeeeee;
    --slate-dark: #263037;
    --slate-mid: #4c5a62;
    --silver: #b9c0c4;
    --green: #4a9a2c;
    --green-light: #7cc242;
    --grey-text: #6a6f72;
    --grey-dark: #4a4f52;
    --band-grey: #55595c;
  }
  * { box-sizing: border-box; margin: 0; padding: 0; }
  html, body { width: 1200px; height: 896px; overflow: hidden; }
  body {
    background: var(--bg);
    font-family: "Cinzel", "Times New Roman", serif;
    position: relative;
  }
  .card {
    position: absolute;
    width: 560px;
    height: 320px;
    background: var(--card);
    box-shadow: 0 6px 18px rgba(0,0,0,0.22);
    overflow: hidden;
  }
  .card--front { left: 70px; top: 130px; }
  .card--back {
    left: 570px; top: 500px;
    background: radial-gradient(ellipse at 50% 45%, #ffffff 0%, #f3f3f3 60%, var(--card-shade) 100%);
  }

  /* front */
  .front-header {
    height: 148px;
    background: linear-gradient(90deg, var(--slate-dark) 0%, var(--slate-mid) 50%, var(--slate-dark) 100%);
    border-bottom: 4px solid var(--silver);
    display: flex;
    align-items: center;
    justify-content: center;
  }
  .firm-mark {
    display: flex;
    align-items: center;
    gap: 12px;
    font-weight: 600;
    letter-spacing: 1px;
  }
  .firm-mark__dot {
    width: 18px; height: 18px; border-radius: 50%;
    background: var(--green-light);
  }
  .firm-mark--light { color: #e9ecee; font-size: 28px; }
  .firm-mark--dark { color: var(--grey-dark); font-size: 28px; }

  .front-body {
    display: flex;
    justify-content: space-between;
    padding: 26px 30px 0 30px;
  }
  .person__name { color: var(--green); font-size: 15px; font-weight: 400; letter-spacing: .5px; }
  .person__title { color: var(--grey-text); font-size: 11px; margin-top: 4px; letter-spacing: .5px; }

  .contact { list-style: none; width: 230px; }
  .contact__item {
    display: flex; align-items: flex-start; gap: 8px;
    color: var(--grey-text); font-size: 10px; line-height: 14px;
    letter-spacing: .4px; margin-bottom: 2px;
  }
  .contact__icon {
    flex: 0 0 11px; width: 11px; height: 11px; margin-top: 1px;
  }
  .contact__lines span { display: block; }

  /* back */
  .back-logo {
    position: absolute; left: 0; right: 0; top: 120px;
    display: flex; justify-content: center;
  }
  .back-band { position: absolute; left: 0; bottom: 22px; width: 560px; height: 20px; }
</style>
</head>
<body>

<section class="card card--front">
  <header class="front-header">
    <div class="firm-mark firm-mark--light">
      <span class="firm-mark__dot"></span>
      <span class="firm-mark__name">The Pettigrew Firm</span>
    </div>
  </header>
  <div class="front-body">
    <div class="person">
      <h1 class="person__name">Marla J. Pettigrew</h1>
      <p class="person__title">Attorney at Law</p>
    </div>
    <ul class="contact">
      <li class="contact__item">
        <svg class="contact__icon" viewBox="0 0 12 12"><circle cx="6" cy="6" r="6" fill="#4a9a2c"/><path d="M6 2.5a2.2 2.2 0 0 0-2.2 2.2C3.8 6.5 6 9.5 6 9.5s2.2-3 2.2-4.8A2.2 2.2 0 0 0 6 2.5z" fill="#fff"/></svg>
        <span class="contact__lines"><span>742 E. 9th Ave, Ste 114</span><span>Spokane, WA 99208</span></span>
      </li>
      <li class="contact__item">
        <svg class="contact__icon" viewBox="0 0 12 12"><circle cx="6" cy="6" r="6" fill="#4a9a2c"/><path d="M4 3l1.2 1.4-.6.8a4 4 0 0 0 1.8 1.8l.8-.6L8.6 7.6 7.8 9A5 5 0 0 1 3 4.2z" fill="#fff"/></svg>
        <span>(509) TRY-CASE</span>
      </li>
      <li class="contact__item">
        <svg class="contact__icon" viewBox="0 0 12 12"><circle cx="6" cy="6" r="6" fill="#4a9a2c"/><rect x="3" y="4" width="6" height="4" fill="#fff"/></svg>
        <span>(509) 555-0148</span>
      </li>
      <li class="contact__item">
        <svg class="contact__icon" viewBox="0 0 12 12"><circle cx="6" cy="6" r="6" fill="#4a9a2c"/><rect x="3" y="4" width="6" height="4.2" fill="#fff"/><path d="M3 4l3 2.2L9 4" stroke="#4a9a2c" stroke-width=".7" fill="none"/></svg>
        <span>barrister@mailwove.com</span>
      </li>
      <li class="contact__item">
        <svg class="contact__icon" viewBox="0 0 12 12"><circle cx="6" cy="6" r="6" fill="#4a9a2c"/><circle cx="6" cy="6" r="3" fill="none" stroke="#fff" stroke-width=".9"/><path d="M3 6h6M6 3v6" stroke="#fff" stroke-width=".7"/></svg>
        <span>www.roadcasedefenders.org</span>
      </li>
    </ul>
  </div>
</section>

<section class="card card--back">
  <div class="back-logo">
    <div class="firm-mark firm-mark--dark">
      <span class="firm-mark__dot"></span>
      <span class="firm-mark__name">The Pettigrew Firm</span>
    </div>
  </div>
  <svg class="back-band" viewBox="0 0 560 20" preserveAspectRatio="none">
    <defs>
      <linearGradient id="bandGreen" x1="0" x2="1">
        <stop offset="0" stop-color="#7cc242"/>
        <stop offset="1" stop-color="#4a9a2c"/>
      </linearGradient>
    </defs>
    <polygon points="0,0 430,0 410,20 0,20" fill="url(#bandGreen)"/>
    <polygon points="436,0 560,0 560,20 416,20" fill="#55595c"/>
  </svg>
</section>

</body>
</html>
```